Business card design needed

My company specialises in carpentry and building services.
Based in Brisbane QLD
We also do:
property maintenance
plastering
painting
tiling
property maintenance

Industry/Entity Type

Carpentry

Contact Information for Business Card

Timberline Trades
Mark 0412583047
Dean 0493217586

```html
<!DOCTYPE html>
<html lang="en">
<head>
<meta charset="utf-8">
<title>Timberline Trades – Business Card</title>
<link rel="stylesheet" href="https://fonts.googleapis.com/css2?family=Oswald:wght@600&family=Comfortaa:wght@400&family=Arimo:wght@700&display=swap">
<style>
  :root {
    --page: #ffffff;
    --wood-light: #c98a45;
    --wood-mid: #b06a2c;
    --wood-dark: #8a4a1c;
    --band: #050505;
    --band-edge: #8a3f1c;
    --pill: #7b331d;
    --pill-edge: #4e1c0d;
    --pill-text: #f6ece2;
    --box: #ffffff;
    --box-text: #0b0b0b;
    --title: #ffffff;
  }
  * { box-sizing: border-box; margin: 0; padding: 0; }
  html, body {
    width: 1200px; height: 1000px; overflow: hidden;
    background: var(--page);
  }
  .canvas { position: relative; width: 1200px; height: 1000px; }

  .card {
    position: absolute; overflow: hidden;
    box-shadow: 6px 8px 10px rgba(0,0,0,0.28);
  }
  .card--front { left: 227px; top: 53px; width: 746px; height: 431px; }
  .card--back  { left: 227px; top: 519px; width: 748px; height: 431px; }

  .wood {
    position: absolute; inset: 0;
    background:
      radial-gradient(ellipse at 50% 45%, rgba(230,170,100,0.45), rgba(0,0,0,0) 65%),
      linear-gradient(90deg, var(--wood-dark), var(--wood-mid) 20%, var(--wood-light) 50%, var(--wood-mid) 80%, var(--wood-dark));
  }

  /* front */
  .title-band {
    position: absolute; left: 0; right: 0; top: 45px; height: 58px;
    border-top: 6px solid var(--band-edge);
    border-bottom: 6px solid var(--band-edge);
    background: var(--band);
    display: flex; align-items: center; justify-content: center;
  }
  .brand {
    font-family: "Oswald", sans-serif; font-weight: 600;
    font-size: 28px; letter-spacing: 1px; color: var(--title);
  }
  .contact { position: absolute; top: 117px; width: 280px; height: 78px; }
  .contact--first { left: 86px; }
  .contact--second { left: 367px; }
  .contact .phone-icon { position: absolute; left: 0; top: 0; width: 60px; height: 78px; }
  .contact .pill {
    position: absolute; left: 30px; top: 13px; width: 245px; height: 54px;
    background: var(--pill); border: 3px solid var(--pill-edge); border-radius: 27px;
    box-shadow: inset 0 3px 6px rgba(0,0,0,0.45);
    display: flex; align-items: center; justify-content: center;
    font-family: "Comfortaa", sans-serif; font-size: 23px; color: var(--pill-text);
    letter-spacing: 0.5px; white-space: nowrap;
  }
  .services {
    position: absolute; left: 30px; top: 244px; list-style: none;
    display: grid; grid-template-columns: 218px 219px 218px;
    column-gap: 15px; row-gap: 33px;
  }
  .service {
    height: 56px; background: var(--box);
    box-shadow: inset 0 0 6px rgba(0,0,0,0.35), 0 1px 2px rgba(0,0,0,0.3);
    display: flex; align-items: center; justify-content: center; text-align: center;
    font-family: "Arimo", sans-serif; font-weight: 700; font-size: 17px;
    line-height: 1.2; letter-spacing: 0.8px; color: var(--box-text);
  }

  /* back */
  .side-band {
    position: absolute; left: 0; top: 0; bottom: 0; width: 63px;
    background: var(--band);
    border-left: 5px solid var(--band-edge);
    border-right: 7px solid var(--band-edge);
  }
  .side-band .brand {
    position: absolute; left: 50%; top: 218px;
    transform: translate(-50%, -50%) rotate(-90deg);
    white-space: nowrap; font-size: 27px;
  }
</style>
</head>
<body>
<div class="canvas">
  <section class="card card--front">
    <div class="wood" role="img" aria-label="Warm wooden floorboard texture"></div>
    <header class="title-band"><span class="brand">TIMBERLINE TRADES</span></header>

    <div class="contact contact--first">
      <svg class="phone-icon" viewBox="0 0 60 78" aria-hidden="true">
        <path d="M14 2 C6 4 2 12 3 24 C5 44 18 64 36 74 C42 77 50 76 54 70 L46 58 C44 56 41 56 39 58 L35 62 C26 56 18 42 16 30 L22 27 C24 26 25 23 24 21 L20 6 C19 3 17 1 14 2 Z" fill="#000"/>
      </svg>
      <div class="pill">Mark 0412583047</div>
    </div>
    <div class="contact contact--second">
      <svg class="phone-icon" viewBox="0 0 60 78" aria-hidden="true">
        <path d="M14 2 C6 4 2 12 3 24 C5 44 18 64 36 74 C42 77 50 76 54 70 L46 58 C44 56 41 56 39 58 L35 62 C26 56 18 42 16 30 L22 27 C24 26 25 23 24 21 L20 6 C19 3 17 1 14 2 Z" fill="#000"/>
      </svg>
      <div class="pill">Dean 0493217586</div>
    </div>

    <ul class="services">
      <li class="service">CARPENTRY</li>
      <li class="service">BUILDING SERVICE</li>
      <li class="service">TILING</li>
      <li class="service">PAINTING</li>
      <li class="service">PLASTERING</li>
      <li class="service">PROPERTY<br>MAINTENANCE</li>
    </ul>
  </section>

  <section class="card card--back">
    <div class="wood" role="img" aria-label="Warm wooden floorboard texture"></div>
    <div class="side-band"><span class="brand">TIMBERLINE TRADES</span></div>
  </section>
</div>
</body>
</html>
```